QRV-TB 2018 Recycling Rate Report

We need a design for our 2018 Recycling Rate Report on Expanded Polystyrene. We want to move from a larger booklet style to a two page document. The report from last year - which was done as a booklet - is attached to provide an example of our style and design.The primary items that must be included (but not limited to) the information on pages 3, 5 & 7. The graphs must include room for 2018 data.To view our typical company design/style please see our website at www.qrvtradeboard.org. Our primary RGB colors are: (187,140,9); (94,47,29); (94,138,164); and (164,167,15). Secondary RGB colors are (249,162,28) and (218,210,208). Our title/header font is DIN Next LT Pro and our copy font is Calibri 10.5 pt. We can deviate from the font specification if beneficial and welcome interesting text treatments and typography.

Target Market(s)

Recycling facilities & general public.

Font styles to use
Sans Serif

Requirements
Must have
• Information presentation must be clean and easy to reference.

```html
<!DOCTYPE html>
<html lang="en">
<head>
<meta charset="utf-8">
<title>QRV-TB 2018 EPS Recycling Rate Report</title>
<link href="https://fonts.googleapis.com/css2?family=Barlow:wght@400;600;700&family=Barlow+Semi+Condensed:wght@400;600;700&family=Carlito:wght@400;700&display=swap" rel="stylesheet">
<style>
  :root{
    --olive:#a4a70f;
    --gold:#bb8c09;
    --brown:#5e2f1d;
    --orange:#f9a21c;
    --mist:#dad2d0;
    --ink:#2b2b2b;
    --paper:#ffffff;
    --stage:#ebe8e5;
  }
  *{box-sizing:border-box;margin:0;padding:0}
  html,body{width:1200px;height:1200px;overflow:hidden;background:var(--stage)}
  body{font-family:"Carlito",Calibri,sans-serif;color:var(--ink)}
  .report{position:absolute;left:0;top:212px;width:1200px;height:776px;background:var(--paper);overflow:hidden}
  .edge-strip{position:absolute;left:0;top:0;width:6px;height:776px;background:var(--olive)}
  .header-band{position:absolute;left:6px;top:0;width:1194px;height:164px;
    background:radial-gradient(circle at 20% 20%,#ffffff 0,#ecebeb 40%,#dcdcdc 100%)}
  .brand{position:absolute;left:43px;top:66px;font-family:"Barlow",sans-serif;font-weight:600;font-size:26px;line-height:1;color:var(--brown);letter-spacing:.3px}
  .title-stack{position:absolute;right:281px;top:22px;text-align:right;font-family:"Barlow Semi Condensed",sans-serif;line-height:.86}
  .title-stack .light{display:block;font-weight:400;font-size:52px;color:var(--gold)}
  .title-stack .strong{display:block;font-weight:700;font-size:50px;color:var(--olive);margin-top:2px}
  .year-ribbon{position:absolute;left:945px;top:25px;width:212px;height:79px}
  .year-ribbon span{position:absolute;left:26px;top:2px;font-family:"Barlow",sans-serif;font-weight:700;font-size:62px;color:#fff;letter-spacing:1px}
  .sub-ribbon{position:absolute;left:945px;top:109px;width:160px;height:40px}
  .sub-ribbon span{position:absolute;left:20px;top:5px;font-family:"Barlow",sans-serif;font-weight:700;font-size:11.5px;line-height:1.2;color:#fff}
  .sidebar{position:absolute;left:6px;top:164px;width:209px;height:612px;background:var(--olive);color:#fff;padding:28px 20px 0 22px}
  .sidebar h2{font-family:"Barlow",sans-serif;font-weight:600;font-size:20px;line-height:1.35;letter-spacing:.2px;margin-bottom:4px}
  .sidebar p{font-size:8.4px;line-height:1.42;text-align:justify;text-indent:6px;margin-bottom:8px}
  .sidebar h2.second{margin-top:14px}
  .section-title{position:absolute;font-family:"Barlow",sans-serif;font-weight:600;font-size:14.5px;color:var(--olive);letter-spacing:.2px}
  .photo-disc{position:absolute;border-radius:50%}
  .stat{position:absolute;text-align:center;font-family:"Barlow",sans-serif}
  .stat .label{font-size:19px;color:var(--ink)}
  .stat .unit{font-family:"Carlito",sans-serif;font-size:9px;color:#444;display:block;margin-top:1px}
  .stat .value{display:block;font-weight:700;font-size:48px;line-height:1.05;margin-top:6px}
  .v-orange{color:var(--orange)}
  .v-olive{color:var(--olive)}
  .dot-rule{position:absolute;border-left:1.5px dotted var(--olive)}
  .chart{position:absolute}
  .callout{position:absolute;background:var(--olive);border-radius:30px;color:#fff;display:flex;align-items:center}
  .callout p{font-size:8.2px;line-height:1.45}
  .data-copy{position:absolute;left:830px;top:221px;width:343px;text-align:right;font-size:8.5px;line-height:1.4}
  .data-photo{position:absolute;left:866px;top:308px;width:140px;height:75px;background:linear-gradient(135deg,#e6e6e6,#c9c9c9)}
  .total{position:absolute;right:35px;top:302px;text-align:right;font-family:"Barlow",sans-serif}
  .total .label{font-size:19px}
  .total .unit{display:block;font-family:"Carlito",sans-serif;font-size:9px;margin-top:-1px}
  .total .value{display:block;font-weight:700;font-size:48px;color:var(--orange);line-height:1.05;margin-top:4px}
  .bar-title{position:absolute;left:835px;top:408px;width:340px;text-align:center;font-family:"Barlow",sans-serif;font-weight:600;font-size:14.5px}
  .bar-sub{position:absolute;left:835px;top:430px;width:340px;text-align:center;font-size:9px}
  .legend{position:absolute;left:868px;top:601px;display:flex;align-items:center;gap:6px;font-family:"Barlow",sans-serif;font-size:8px;text-transform:uppercase}
  .legend i{display:inline-block;width:24px;height:24px;border-radius:50%}
  .legend .gap{width:18px}
</style>
</head>
<body>
<main class="report">
  <div class="edge-strip"></div>
  <div class="header-band" role="img" aria-label="Photographic backdrop of white polystyrene beads"></div>

  <div class="brand">QRV Trade Board</div>

  <h1 class="title-stack">
    <span class="light">TAKE</span>
    <span class="light">A LOOK AT</span>
    <span class="strong">EPS RECYCLING</span>
  </h1>

  <div class="year-ribbon">
    <svg width="212" height="79" viewBox="0 0 212 79"><polygon points="0,0 212,0 178,39.5 212,79 0,79" fill="var(--gold)"/><rect width="6" height="79" fill="var(--brown)"/></svg>
    <span>2018</span>
  </div>
  <div class="sub-ribbon">
    <svg width="160" height="40" viewBox="0 0 160 40"><polygon points="0,0 145,0 160,20 145,40 0,40" fill="var(--olive)"/><rect width="6" height="40" fill="#6f7109"/></svg>
    <span>EPS RECYCLING<br>RATE REPORT</span>
  </div>

  <aside class="sidebar">
    <h2>METHODOLOGY</h2>
    <p>The 2017 Expanded Polystyrene Recycling Rate Study was conducted by the QRV Trade Board to gather data to reflect both post-consumer and post-industrial recycling activity. The 2017 results are based on data received from 55 EPS manufacturers and independent recyclers in the U.S.</p>
    <p>Participation in the EPS recycling survey is voluntary and the reported data is based on the responses received. Many companies have limited resources to put towards participation in the survey, and some companies may choose not to respond due to their confidentiality policies. Therefore, because there is not 100 percent participation, the presented totals represent the minimum amount of EPS recovered for recycling.</p>
    <h2 class="second">COLLECTION<br>OPTIONS &amp;<br>RESOURCES</h2>
    <p>Not everything can be recycled all the time. In order for materials to be recycled, stable markets must exist and there must be a demand for the end products. Each community has its own guidelines for which plastics are accepted, and these can vary widely. Some locations also offer consumer drop-off access. To find out if EPS recycling is available in your area, visit www.qrvtradeboard.org.</p>
    <p>For consumers that do not have access to a local drop-off center, the QRV-TB sponsors a National Mail-Back Program intended for smaller quantities of EPS which can be mailed via NPX or QPS to more than 20 locations nationwide. Full instructions and a list of Mail-Back locations are available on the QRV-TB website.</p>
  </aside>

  <h2 class="section-title" style="left:349px;top:196px">POST-CONSUMER EPS RECYCLING 1990-2018</h2>

  <div class="photo-disc" role="img" aria-label="Photo of stacked white EPS scrap in a recycling facility" style="left:236px;top:232px;width:124px;height:124px;border:4px solid var(--orange);background:radial-gradient(circle,#e8e8e8,#7a7a7a)"></div>
  <div class="stat" style="left:355px;top:255px;width:140px">
    <span class="label">Post-Industrial</span><span class="unit">(millions of pounds)</span>
    <span class="value v-orange">39.0</span>
  </div>
  <div class="dot-rule" style="left:505px;top:250px;height:88px"></div>
  <div class="stat" style="left:512px;top:255px;width:140px">
    <span class="label">Post-Consumer</span><span class="unit">(millions of pounds)</span>
    <span class="value v-olive">30.0</span>
  </div>
  <div class="photo-disc" role="img" aria-label="Photo of a worker handling a large sheet of EPS foam" style="left:658px;top:234px;width:120px;height:120px;background:radial-gradient(circle at 40% 45%,#efefef,#4a4a4a)"></div>

  <svg class="chart" style="left:255px;top:420px" width="520" height="232" viewBox="0 0 520 232" font-family="Carlito, sans-serif">
    <g stroke="#e2e2e2" stroke-width="0.8">
      <line x1="16" y1="10" x2="16" y2="212"/><line x1="49.4" y1="10" x2="49.4" y2="212"/><line x1="82.3" y1="10" x2="82.3" y2="212"/><line x1="115.2" y1="10" x2="115.2" y2="212"/><line x1="148" y1="10" x2="148" y2="212"/><line x1="180.9" y1="10" x2="180.9" y2="212"/><line x1="213.8" y1="10" x2="213.8" y2="212"/><line x1="246.6" y1="10" x2="246.6" y2="212"/><line x1="279.5" y1="10" x2="279.5" y2="212"/><line x1="312.3" y1="10" x2="312.3" y2="212"/><line x1="345.2" y1="10" x2="345.2" y2="212"/><line x1="378" y1="10" x2="378" y2="212"/><line x1="410.9" y1="10" x2="410.9" y2="212"/><line x1="443.8" y1="10" x2="443.8" y2="212"/><line x1="476.6" y1="10" x2="476.6" y2="212"/><line x1="509.5" y1="10" x2="509.5" y2="212"/>
    </g>
    <g font-size="7" fill="#5a5a00" text-anchor="end">
      <text x="10" y="211">0</text><text x="10" y="184">10</text><text x="10" y="156">20</text><text x="10" y="129">30</text><text x="10" y="101">40</text><text x="10" y="73">50</text><text x="10" y="46">60</text><text x="10" y="18">70</text>
    </g>
    <text x="-110" y="-4" font-size="6" fill="#666" transform="rotate(-90)" text-anchor="middle">Millions of Pounds Recycled</text>
    <polyline fill="none" stroke="var(--olive)" stroke-width="1.4" points="33,200.7 65.9,151.7 98.7,142.3 131.6,147 164.4,158.8 197.3,140.4 230.2,136.8 263,140.1 295.9,120.8 328.7,116.4 361.6,106.7 394.5,107.8 427.3,35.3 460.2,137.6 493,126.3"/>
    <g fill="var(--orange)">
      <circle cx="33" cy="200.7" r="2.5"/><circle cx="65.9" cy="151.7" r="2.5"/><circle cx="98.7" cy="142.3" r="2.5"/><circle cx="131.6" cy="147" r="2.5"/><circle cx="164.4" cy="158.8" r="2.5"/><circle cx="197.3" cy="140.4" r="2.5"/><circle cx="230.2" cy="136.8" r="2.5"/><circle cx="263" cy="140.1" r="2.5"/><circle cx="295.9" cy="120.8" r="2.5"/><circle cx="328.7" cy="116.4" r="2.5"/><circle cx="361.6" cy="106.7" r="2.5"/><circle cx="394.5" cy="107.8" r="2.5"/><circle cx="427.3" cy="35.3" r="2.5"/><circle cx="460.2" cy="137.6" r="2.5"/><circle cx="493" cy="126.3" r="4.5"/>
    </g>
    <g font-size="7.5" fill="#333" text-anchor="middle">
      <text x="37" y="189">3.0</text><text x="65.9" y="144">20.8</text><text x="98.7" y="134">24.2</text><text x="131.6" y="139">22.5</text><text x="164.4" y="151">18.2</text><text x="197.3" y="132">24.9</text><text x="230.2" y="128">26.2</text><text x="263" y="132">25.0</text><text x="295.9" y="112">32.0</text><text x="328.7" y="108">33.6</text><text x="361.6" y="98">37.1</text><text x="390" y="98">36.7</text><text x="427.3" y="26">63.0</text><text x="460.2" y="152">25.9</text><text x="493" y="141">30.0</text>
    </g>
    <g font-size="7.5" fill="#333" text-anchor="middle">
      <text x="33" y="225">1990</text><text x="65.9" y="225">1992</text><text x="98.7" y="225">1994</text><text x="131.6" y="225">1996</text><text x="164.4" y="225">1998</text><text x="197.3" y="225">2000</text><text x="230.2" y="225">2002</text><text x="263" y="225">2004</text><text x="295.9" y="225">2006</text><text x="328.7" y="225">2008</text><text x="361.6" y="225">2010</text><text x="394.5" y="225">2012</text><text x="427.3" y="225">2016</text><text x="460.2" y="225">2017</text><text x="493" y="225">2018</text>
    </g>
  </svg>

  <div class="callout" style="left:272px;top:682px;width:488px;height:56px;padding:0 22px 0 12px">
    <svg width="40" height="36" viewBox="0 0 40 36" style="flex:none;margin-right:18px"><path d="M4 30 L4 18 Q4 10 12 10 L26 10 L26 3 L37 14 L26 25 L26 18 L14 18 Q12 18 12 20 L12 30 Z" fill="none" stroke="#fff" stroke-width="1.6" stroke-linejoin="round"/></svg>
    <p>The 25-year baseline shows incremental gains with more than 23 million pounds of EPS recycled annually on average. Like all commodity markets, the EPS recycling market is cyclical. The 2017 results reflect a decrease from 2016 due to the new landscape for recycling commodities and changing international markets, especially in China.</p>
  </div>

  <div class="dot-rule" style="left:797px;top:236px;height:500px"></div>

  <h2 class="section-title" style="right:35px;top:196px">DATA</h2>
  <p class="data-copy">More than 89 million pounds of EPS were recycled during calendar year 2018. This figure includes 25.9 million pounds of post-consumer packaging and 39.0 million pounds of post-industrial recovery. Post-consumer is defined as any material that is recycled after its intended end-use while post-industrial recovery includes EPS facility scrap that is recycled but never served its intended purpose as a packaging material or other end-use application.</p>
  <div class="data-photo" role="img" aria-label="Close-up photo of a molded resin code on EPS foam"></div>
  <div class="total">
    <span class="label">2018 Total</span><span class="unit">million pounds of EPS recycled</span>
    <span class="value">89.0</span>
  </div>

  <h3 class="bar-title">EPS Recycling Post-Consumer &amp; Post-Industrial</h3>
  <p class="bar-sub">(millions of pounds)</p>

  <svg class="chart" style="left:815px;top:455px" width="360" height="140" viewBox="0 0 360 140" font-family="Carlito, sans-serif">
    <line x1="2" y1="123" x2="358" y2="123" stroke="#bbb" stroke-width="0.8"/>
    <g fill="var(--olive)">
      <rect x="7" y="76.4" width="17" height="46.6"/><rect x="57.5" y="76.2" width="17" height="46.8"/><rect x="108" y="60.1" width="17" height="62.9"/><rect x="158.5" y="54.3" width="17" height="68.7"/><rect x="209" y="5" width="17" height="118"/><rect x="259.5" y="74.5" width="17" height="48.5"/><rect x="310" y="54.3" width="17" height="68.7"/>
    </g>
    <g fill="var(--orange)">
      <rect x="25" y="93.8" width="17" height="29.2"/><rect x="75.5" y="61.2" width="17" height="61.8"/><rect x="126" y="57.4" width="17" height="65.6"/><rect x="176.5" y="18.1" width="17" height="104.9"/><rect x="227" y="18.1" width="17" height="104.9"/><rect x="277.5" y="50" width="17" height="73"/><rect x="328" y="18.1" width="17" height="104.9"/>
    </g>
    <g font-size="4.5" text-anchor="middle" fill="var(--olive)">
      <text x="15.5" y="74">24.9</text><text x="66" y="74">25.0</text><text x="116.5" y="58">33.6</text><text x="167" y="52">36.7</text><text x="217.5" y="3.5">63.0</text><text x="268" y="72">25.9</text><text x="318.5" y="52">36.7</text>
    </g>
    <g font-size="4.5" text-anchor="middle" fill="var(--orange)">
      <text x="33.5" y="91.5">15.6</text><text x="84" y="59">33.0</text><text x="134.5" y="55">35.0</text><text x="185" y="16">56.0</text><text x="235.5" y="16">56.0</text><text x="286" y="48">39.0</text><text x="336.5" y="16">56.0</text>
    </g>
    <g font-size="5" font-weight="700" text-anchor="middle" fill="#333">
      <text x="24.5" y="131">2000</text><text x="75" y="131">2004</text><text x="125.5" y="131">2008</text><text x="176" y="131">2012</text><text x="226.5" y="131">2016</text><text x="277" y="131">2017</text><text x="327.5" y="131">2018</text>
    </g>
  </svg>

  <div class="legend">
    <i style="background:var(--olive)"></i><span>— Post-Consumer</span>
    <span class="gap"></span>
    <i style="background:var(--orange)"></i><span>— Post-Industrial</span>
  </div>

  <div class="callout" style="left:825px;top:639px;width:347px;height:99px;border-radius:50px;padding:0 24px 0 14px">
    <svg width="40" height="36" viewBox="0 0 40 36" style="flex:none;margin-right:20px"><path d="M4 30 L4 18 Q4 10 12 10 L26 10 L26 3 L37 14 L26 25 L26 18 L14 18 Q12 18 12 20 L12 30 Z" fill="none" stroke="#fff" stroke-width="1.6" stroke-linejoin="round"/></svg>
    <p style="text-align:justify">Despite lower collection amounts reflected in 2017, EPS has historically enjoyed consistent growth since its inception in the early 1990's. This decrease is a direct result of export restrictions on recycled plastics and a reprocessing plant closure that previously recycled large quantities of EPS. Newer EPS recycling technologies to facilitate EPS collection and reprocessing launched in 2018 indicate growth rates will continue on an upward trend in the future.</p>
  </div>
</main>
</body>
</html>
```